Memoir author looking for book cover design

Title:
"Tides, Thorns and Twilight"

Subtitle:
"The Journey to Reach my Brother, Vanished on the Glacier"

My book is about the 18-month-long search and grieving process after my husband went missing from a hiking accident.
See "notesbeyondthequietfjord.example" for background

(An "ampersand" may look best, but I'm unable to enter it in this format)

Reason: Having difficulty finishing up, in part due to time difference. Don't want designers to have to work in the middle of the night!

```html
<!DOCTYPE html>
<html lang="en">
<head>
<meta charset="utf-8">
<title>Tides, Thorns and Twilight — Cover Spread</title>
<link rel="stylesheet" href="https://fonts.googleapis.com/css2?family=Dosis:wght@600;700&family=Quicksand:wght@500;600;700&display=swap">
<style>
  :root {
    --page-bg: #e7e4df;
    --ink-white: #ffffff;
    --accent-orange: #f39a2c;
    --spine-grey: #4a4a4d;
    --spine-grey-deep: #2f2f31;
    --sky-top: #3f6d9e;
    --sky-mid: #7d93a8;
    --horizon: #e9923a;
    --ground: #0b0c0f;
  }
  * { margin: 0; padding: 0; box-sizing: border-box; }
  html, body { width: 880px; height: 1200px; overflow: hidden; background: var(--page-bg); }
  .spread {
    position: absolute; left: 0; top: 290px;
    width: 880px; height: 621px;
    background: var(--ground);
    overflow: hidden;
    font-family: "Quicksand", sans-serif;
    color: var(--ink-white);
  }
  .back-cover, .spine, .front-cover { position: absolute; top: 0; height: 100%; }
  .back-cover { left: 0; width: 408px; }
  .spine { left: 408px; width: 64px; background: linear-gradient(180deg, var(--spine-grey) 0%, var(--spine-grey) 60%, var(--spine-grey-deep) 100%); }
  .front-cover { left: 472px; width: 408px; }
  .photo { position: absolute; inset: 0; width: 100%; height: 100%; }
  .back-photo { background: linear-gradient(180deg, var(--sky-top) 0%, #5a7fa3 22%, #1a2028 30%, #08090b 46%, var(--ground) 100%); }
  .front-photo { background: linear-gradient(180deg, var(--sky-top) 0%, var(--sky-mid) 38%, var(--horizon) 47%, #3a3c44 53%, #14161b 64%, var(--ground) 100%); }

  .blurb {
    position: absolute; left: 30px; top: 290px; width: 348px;
    font-size: 10.6px; line-height: 14px; font-weight: 500;
    text-align: justify;
  }
  .blurb-heading { text-transform: uppercase; text-align: left; }
  .blurb p + p { margin-top: 14px; }

  .spine-title-word {
    position: absolute; top: 226px; left: 0; width: 100%;
    text-align: center; font-size: 22px; font-weight: 600;
  }
  .spine-text {
    position: absolute; top: 256px; left: 10px; height: 200px;
    writing-mode: vertical-rl;
    line-height: 11px;
  }
  .spine-text .spine-title { font-family: "Dosis", sans-serif; font-weight: 700; font-size: 15px; line-height: 17px; color: var(--accent-orange); letter-spacing: 0.5px; }
  .spine-text .spine-subtitle { font-size: 8.5px; font-weight: 600; }

  .cover-title { position: absolute; left: 46px; top: 392px; width: 340px; }
  .title-small {
    display: block; text-align: right; padding-right: 8px;
    font-family: "Dosis", sans-serif; font-weight: 700;
    font-size: 31px; line-height: 31px; letter-spacing: 0.5px;
    color: var(--accent-orange);
  }
  .title-large {
    display: block; margin-top: -14px;
    font-size: 110px; line-height: 104px; font-weight: 700; letter-spacing: -2px;
  }
  .cover-subtitle {
    position: absolute; left: 0; top: 518px; width: 408px;
    text-align: center; font-size: 18px; line-height: 25px; font-weight: 600;
  }
  .cover-subtitle .accent { color: var(--accent-orange); }
</style>
</head>
<body>
  <section class="spread">
    <div class="back-cover">
      <div class="photo back-photo" role="img" aria-label="Photograph of a jagged mountain ridge silhouetted against a blue dusk sky"></div>
      <div class="blurb">
        <p><span class="blurb-heading">Where does it come from?</span><br>
        Contrary to popular belief, Lorem Ipsum is not simply random text. It has roots in a piece of classical Latin literature from 45 BC, making it over 2000 years old. Edwin Harlowe, a Latin professor at Larkmoor College in Vermont, looked up one of the more obscure Latin words, consectetur, from a Lorem Ipsum passage, and going through the cites of the word in classical literature, discovered the undoubtable source. Lorem Ipsum comes from sections 1.10.32 and 1.10.33 of "de Finibus Bonorum et Malorum" (The Extremes of Good and Evil) by Aurelian, written in 45 BC. This book is a treatise on the theory of ethics, very popular during the Renaissance. The first line of Lorem Ipsum, "Lorem ipsum dolor sit amet..", comes from a line in section 1.10.32.</p>
        <p>The standard chunk of Lorem Ipsum used since the 1500s is reproduced below for those interested. Sections 1.10.32 and 1.10.33 from "de Finibus Bonorum et Malorum" by Aurelian are also reproduced in their exact original form, accompanied by English versions from the 1914 translation by J. Penrose.</p>
      </div>
    </div>

    <div class="spine">
      <div class="spine-title-word">Tides</div>
      <div class="spine-text">
        <div class="spine-title">THORNS AND TWILIGHT</div>
        <div class="spine-subtitle">The Journey to Reach my Brother,</div>
        <div class="spine-subtitle">Vanished on the Glacier</div>
      </div>
    </div>

    <div class="front-cover">
      <div class="photo front-photo" role="img" aria-label="Photograph of a hooded hiker seen from behind, silhouetted against a sunset over a sea of clouds"></div>
      <h1 class="cover-title">
        <span class="title-small">THORNS AND TWILIGHT</span>
        <span class="title-large">Tides</span>
      </h1>
      <p class="cover-subtitle">The Journey to Reach my Brother,<br><span class="accent">Vanished</span> on the Glacier</p>
    </div>
  </section>
</body>
</html>
```